Modern business card for triathlon training business in Australia

We need a business card design for our triathlon training company.

Pace with Us Fitness is an Australian business, owned by women, run for women. Pace with Us Fitness helps women prepare or improve triathlon skills and confidence through triathlon camps completely designed for women.

Our camps focus on preparing women both physically and mentally for their next (or first!) triathlon.

You can see our website www.pacewithusfitness.com.au for more info about our business and our style.

We've attached two of our logos and are happy to consider a design that utilised either colour scheme with the teal colour being our 'feature' colour. We don't want overly feminine cards but rather cards that are professional and neat. If the inclusion of any pictures/art is warranted, this should be focused on our swim/ride/run theme and in that specific order (swim/ride/run).

The business card needs to be a printable design and the contact details will need to change for our two employees.

Target Market(s)

Female clients and partners/vendors/sponsors that we work with in the triathlon industry

Industry/Entity Type

Fitness

Contact Information for Business Card

Pace with Us Fitness (business name)
Nina Carver
Business Director
Mobile: 0438 916 207
Email: nina@pacewithusfitness.com.au
www.pacewithusfitness.com.au

Second business card:
Pace with Us Fitness
Bel Stray
Coaching Director
Mobile: 0459 260 718
Email: bel@pacewithusfitness.com.au

Font styles to use
Serif
Sans Serif

Requirements
Must have
• Core contact details above, our logo and be a printable design
Should not have
• Pink
• Cursive/script fonts

```html
<!DOCTYPE html>
<html lang="en">
<head>
<meta charset="utf-8">
<title>Pace with Us Fitness — Business Card</title>
<link rel="stylesheet" href="https://fonts.googleapis.com/css2?family=Open+Sans:wght@400;600;700&display=swap">
<style>
  :root {
    --bg: #e6e4e0;
    --card-black: #0d0e10;
    --card-black-soft: #1c1e22;
    --teal: #2fc6d4;
    --teal-deep: #1aa6b4;
    --white: #f4f6f7;
    --grey-light: #d9dcde;
    --photo-a: #8f9488;
    --photo-b: #c9ccc8;
  }
  * { box-sizing: border-box; margin: 0; padding: 0; }
  html, body {
    width: 1200px; height: 1022px; overflow: hidden;
    background: var(--bg);
    font-family: "Open Sans", Arial, sans-serif;
  }
  .sheet {
    position: relative; width: 1200px; height: 1022px;
    display: flex; flex-direction: column; align-items: center; justify-content: center; gap: 50px;
  }
  .card {
    position: relative; width: 740px; height: 452px; overflow: hidden;
    background: linear-gradient(160deg, var(--card-black-soft) 0%, var(--card-black) 60%);
    box-shadow: 0 10px 28px rgba(0,0,0,.25);
  }
  .card-art { position: absolute; inset: 0; width: 100%; height: 100%; }

  /* Front */
  .person { position: absolute; left: 60px; top: 190px; }
  .person-name { color: var(--white); font-weight: 700; font-size: 40px; letter-spacing: .5px; }
  .person-role { color: var(--teal); font-weight: 700; font-size: 22px; margin-top: 2px; }

  /* Back */
  .brand {
    position: absolute; left: 56px; top: 60px;
    display: flex; align-items: center; gap: 16px;
  }
  .brand-dot { width: 46px; height: 46px; border-radius: 50%; background: var(--teal); }
  .brand-name { color: var(--teal); font-weight: 700; font-size: 30px; text-transform: uppercase; letter-spacing: 1px; }
  .contact {
    position: absolute; right: 56px; bottom: 70px; text-align: right;
    color: var(--white); font-size: 22px; line-height: 1.6;
  }
  .contact-icons { display: flex; justify-content: flex-end; gap: 14px; margin-bottom: 14px; }
  .contact-icons svg { width: 24px; height: 24px; }
</style>
</head>
<body>
<main class="sheet">

  <!-- Front -->
  <section class="card card-front">
    <svg class="card-art" viewBox="0 0 740 452" preserveAspectRatio="none">
      <defs>
        <linearGradient id="photoTone" x1="0" y1="0" x2="1" y2="1">
          <stop offset="0" stop-color="var(--photo-a)"/>
          <stop offset="1" stop-color="var(--photo-b)"/>
        </linearGradient>
        <linearGradient id="paleTone" x1="0" y1="0" x2="1" y2="1">
          <stop offset="0" stop-color="#ffffff"/>
          <stop offset="1" stop-color="var(--grey-light)"/>
        </linearGradient>
      </defs>
      <polygon points="660,0 740,0 740,452 560,452" fill="url(#paleTone)"/>
      <polygon points="440,0 660,0 560,452 340,452" fill="url(#photoTone)" role="img" aria-label="Photo of a triathlete riding a bike in a race"/>
      <polygon points="428,0 440,0 340,452 328,452" fill="var(--teal)"/>
      <polygon points="660,0 672,0 572,452 560,452" fill="var(--teal)"/>
    </svg>
    <div class="person">
      <p class="person-name">Nina Carver</p>
      <p class="person-role">Business Director</p>
    </div>
  </section>

  <!-- Back -->
  <section class="card card-back">
    <svg class="card-art" viewBox="0 0 740 452" preserveAspectRatio="none">
      <line x1="0" y1="330" x2="140" y2="452" stroke="var(--teal)" stroke-width="6"/>
    </svg>
    <div class="brand">
      <span class="brand-dot"></span>
      <span class="brand-name">Pace with Us Fitness</span>
    </div>
    <div class="contact">
      <div class="contact-icons">
        <svg viewBox="0 0 24 24" aria-label="Phone"><rect x="6" y="2" width="12" height="20" rx="2" fill="none" stroke="var(--teal)" stroke-width="2"/><circle cx="12" cy="18" r="1.2" fill="var(--teal)"/></svg>
        <svg viewBox="0 0 24 24" aria-label="Web"><circle cx="12" cy="12" r="9" fill="none" stroke="var(--teal)" stroke-width="2"/><ellipse cx="12" cy="12" rx="4" ry="9" fill="none" stroke="var(--teal)" stroke-width="1.6"/><line x1="3" y1="12" x2="21" y2="12" stroke="var(--teal)" stroke-width="1.6"/></svg>
        <svg viewBox="0 0 24 24" aria-label="Email"><rect x="2" y="5" width="20" height="14" fill="none" stroke="var(--teal)" stroke-width="2"/><polyline points="2,5 12,13 22,5" fill="none" stroke="var(--teal)" stroke-width="2"/></svg>
      </div>
      <p class="contact-phone">0438 916 207</p>
      <p class="contact-web">www.pacewithusfitness.com.au</p>
      <p class="contact-email">nina@pacewithusfitness.com.au</p>
    </div>
  </section>

</main>
</body>
</html>
```